Modern Spot UV Business Card design

We are a relatively new real estate agency. We need a business card that reflects the professionalism and prestige of our company but is also modern and fresh, based around our logo.
We would love to utilise spot UV.
Happy to let the designers use their imagination and see what they come up with (we're not very creative, so have no ideas for you, sorry) :-)
We'd like one for each staff member, but I've just provided one staff members photo here to avoid confusion.

Target Market(s)

Families

Industry/Entity Type

Real Estate Agent

Contact Information for Business Card

Colin Varga - Director & Principal
Mobile: 0491 527 806
Email: colin.varga@vbrokers.example.com.au
Phone: (08) 7364 9150
Fax: (08) 7364 9182
www.vargabrokersrealestate.example.com.au

Font styles to use
Other font styles liked:
• Kabel Dm BT

Requirements
Must have
• Contact details, logo, photo, spot UV
Nice to have
• Modern interesting features that will make people comment. Nothing too feminine nor too masculine.
Should not have
• No houses! Nothing typical of a real estate agent.

```html
<!DOCTYPE html>
<html lang="en">
<head>
<meta charset="utf-8">
<title>Varga Brokers Real Estate – Business Card</title>
<link rel="stylesheet" href="https://fonts.googleapis.com/css2?family=Montserrat:wght@600;700;800&family=Open+Sans:wght@400;600&display=swap">
<style>
  :root {
    --bg: #e4e4e4;
    --card: #f7f7f7;
    --ink: #1f1f1f;
    --grey: #9a9a9a;
    --grey-dark: #6f6f6f;
    --blue: #1b8fd2;
    --orange: #ec8a1c;
    --yellow: #e4c21a;
    --white: #ffffff;
  }
  * { box-sizing: border-box; margin: 0; padding: 0; }
  html, body { width: 1200px; height: 1000px; overflow: hidden; }
  body {
    background: var(--bg);
    font-family: "Open Sans", Arial, sans-serif;
    position: relative;
  }
  .card {
    position: absolute;
    top: 170px;
    width: 400px;
    height: 660px;
    background: var(--card);
    box-shadow: 0 6px 18px rgba(0,0,0,.12);
    overflow: hidden;
  }
  .card--front { left: 150px; }
  .card--back { left: 650px; }

  /* Front */
  .portrait {
    position: absolute;
    top: 50px; left: 75px;
    width: 250px; height: 250px;
  }
  .portrait__photo {
    position: absolute; inset: 10px;
    border-radius: 50%;
    background: linear-gradient(180deg, #ececec 0%, #d8c4b4 45%, #5a5d62 100%);
  }
  .portrait__ring { position: absolute; inset: 0; }
  .name-band {
    position: absolute; top: 340px; left: 0; right: 0;
    height: 36px; background: var(--grey);
    color: var(--white);
    font-family: "Montserrat", Arial, sans-serif; font-weight: 700;
    font-size: 17px; letter-spacing: .5px;
    display: flex; align-items: center; justify-content: center;
  }
  .brand {
    position: absolute; left: 0; right: 0;
    display: flex; flex-direction: column; align-items: center;
  }
  .card--front .brand { top: 410px; }
  .card--back .brand { top: 455px; }
  .brand__row { display: flex; align-items: center; gap: 10px; }
  .brand__dot { width: 22px; height: 22px; border-radius: 50%; background: var(--orange); flex: none; }
  .brand__name {
    font-family: "Montserrat", Arial, sans-serif; font-weight: 800;
    color: var(--ink); font-size: 30px; line-height: 1.05; text-align: left;
  }
  .brand__tagline {
    margin-top: 8px; color: var(--grey-dark);
    font-size: 13px; letter-spacing: .3px;
  }
  .website {
    position: absolute; top: 572px; left: 28px;
    display: flex; align-items: center; gap: 8px;
    font-size: 14px; color: var(--grey-dark);
  }
  .stripes { position: absolute; bottom: 0; left: 0; right: 0; }
  .stripes span { display: block; height: 6px; }
  .stripe--orange { background: var(--orange); }
  .stripe--blue { background: var(--blue); }
  .stripe--yellow { background: var(--yellow); }
  .stripe--gap { background: var(--card); height: 3px !important; }

  /* Back */
  .person {
    position: absolute; top: 50px; left: 40px;
    display: flex; align-items: center; gap: 16px;
  }
  .person__avatar {
    width: 66px; height: 66px; border-radius: 50%;
    background: var(--blue);
    display: flex; align-items: center; justify-content: center;
  }
  .person__name {
    font-family: "Montserrat", Arial, sans-serif; font-weight: 800;
    font-size: 27px; color: var(--ink); line-height: 1.1;
  }
  .person__name .surname { color: var(--blue); }
  .person__title {
    font-family: "Montserrat", Arial, sans-serif; font-weight: 700;
    font-size: 15px; color: #333;
  }
  .person__rule { margin-top: 10px; width: 110px; height: 3px; background: var(--blue); }
  .contacts { position: absolute; top: 175px; left: 0; right: 0; list-style: none; }
  .contact {
    height: 44px; display: flex; align-items: center; gap: 18px;
    padding-left: 34px; color: var(--white);
    font-size: 15px; letter-spacing: .6px;
  }
  .contact svg { width: 22px; height: 22px; flex: none; }
  .contact--mobile { background: var(--blue); }
  .contact--phone { background: var(--orange); }
  .contact--email { background: var(--grey-dark); font-size: 13px; letter-spacing: .2px; }
  .contact--fax { background: var(--yellow); }
  .accent-line {
    position: absolute; top: 610px; left: 110px;
    width: 220px; height: 3px;
    background: linear-gradient(90deg, transparent, var(--orange) 40%, var(--orange) 70%, transparent);
  }
</style>
</head>
<body>

<section class="card card--front" aria-label="Card front">
  <div class="portrait">
    <div class="portrait__photo" role="img" aria-label="Portrait photo of Colin Varga"></div>
    <svg class="portrait__ring" viewBox="0 0 250 250" aria-hidden="true">
      <circle cx="125" cy="125" r="121" fill="none" stroke="var(--blue)" stroke-width="4"/>
      <path d="M4 125 A121 121 0 0 1 125 4" fill="none" stroke="var(--orange)" stroke-width="4"/>
      <path d="M246 125 A121 121 0 0 1 170 237" fill="none" stroke="var(--yellow)" stroke-width="4"/>
    </svg>
  </div>
  <div class="name-band">Colin Varga</div>
  <div class="brand">
    <div class="brand__row">
      <span class="brand__dot"></span>
      <span class="brand__name">Varga Brokers<br>Real Estate</span>
    </div>
    <p class="brand__tagline">Guiding you to your new address</p>
  </div>
  <div class="website">
    <svg width="16" height="16" viewBox="0 0 16 16" aria-hidden="true">
      <circle cx="8" cy="8" r="7" fill="var(--blue)"/>
      <g fill="none" stroke="#fff" stroke-width="1">
        <ellipse cx="8" cy="8" rx="3" ry="7"/><line x1="1" y1="8" x2="15" y2="8"/>
        <line x1="2.5" y1="4.5" x2="13.5" y2="4.5"/><line x1="2.5" y1="11.5" x2="13.5" y2="11.5"/>
      </g>
    </svg>
    <span>www.vargabrokersrealestate.example.com.au</span>
  </div>
  <div class="stripes" aria-hidden="true">
    <span class="stripe--orange"></span><span class="stripe--gap"></span>
    <span class="stripe--blue"></span><span class="stripe--gap"></span>
    <span class="stripe--yellow"></span>
  </div>
</section>

<section class="card card--back" aria-label="Card back">
  <div class="person">
    <div class="person__avatar">
      <svg width="40" height="40" viewBox="0 0 40 40" aria-hidden="true">
        <circle cx="20" cy="14" r="8" fill="#fff"/>
        <path d="M5 36 C5 25 12 22 20 22 C28 22 35 25 35 36 Z" fill="#fff"/>
      </svg>
    </div>
    <div>
      <h1 class="person__name">Colin <span class="surname">Varga</span></h1>
      <p class="person__title">Director &amp; Principal</p>
      <div class="person__rule"></div>
    </div>
  </div>
  <ul class="contacts">
    <li class="contact contact--mobile">
      <svg viewBox="0 0 22 22" aria-hidden="true"><rect x="6" y="2" width="10" height="18" rx="2" fill="none" stroke="#fff" stroke-width="1.6"/><circle cx="11" cy="17" r="1" fill="#fff"/></svg>
      <span>0491 527 806</span>
    </li>
    <li class="contact contact--phone">
      <svg viewBox="0 0 22 22" aria-hidden="true"><path d="M5 3 L9 3 L10 8 L7.5 9.5 C8.5 12 10 13.5 12.5 14.5 L14 12 L19 13 L19 17 C19 18 18 19 17 19 C9.5 18.5 3.5 12.5 3 5 C3 4 4 3 5 3 Z" fill="#fff"/></svg>
      <span>(08) 7364 9150</span>
    </li>
    <li class="contact contact--email">
      <svg viewBox="0 0 22 22" aria-hidden="true"><rect x="2" y="5" width="18" height="12" fill="#fff"/><path d="M2 5 L11 12 L20 5" fill="none" stroke="var(--grey-dark)" stroke-width="1.4"/></svg>
      <span>colin.varga@vbrokers.example.com.au</span>
    </li>
    <li class="contact contact--fax">
      <svg viewBox="0 0 22 22" aria-hidden="true"><rect x="6" y="3" width="10" height="6" fill="#fff"/><rect x="2" y="9" width="18" height="10" rx="1.5" fill="#fff"/><rect x="6" y="12" width="10" height="1.4" fill="var(--yellow)"/><rect x="6" y="15" width="10" height="1.4" fill="var(--yellow)"/></svg>
      <span>(08) 7364 9182</span>
    </li>
  </ul>
  <div class="brand">
    <div class="brand__row">
      <span class="brand__dot"></span>
      <span class="brand__name">Varga Brokers<br>Real Estate</span>
    </div>
    <p class="brand__tagline">Guiding you to your new address</p>
  </div>
  <div class="accent-line" aria-hidden="true"></div>
</section>

</body>
</html>
```